Webdesign für Veredelung von Betonoberflächen
Zielgruppe
Die KORVAN Industrieboden GmbH hat sich auf das Polieren und Veredeln von Betonoberflächen und anderen Untergründen spezialisiert.
Aufgabenstellung
- Design als PSD
- Bilder sollen dominieren - Text eher weniger, 'cool gestylt'
- Slogan: 'Wer aufhört, besser zu werden, hat aufgehört, gut zu sein' Lorenz Haberkamp
- die Website soll den Fokus auf technisches Know How, hohe Leistungsfähigkeit mit modernem Maschinenpark
- leider liegt uns das Logo noch nicht vor, bitte aus der derzeitigen Website entnehmen
- SM-Kanäle einarbeiten ( FB, Berufo, Xantel, Insta)
- Website gefällt: https://www.mivoda.de/ (nicht kopieren!)
-* mit dem Logo des Partners brunnwald International GmbH - siehe https://www.brunnwald-international.de/
- WICHTIG: dominante Darstellung der Logos von http://www.tremlow-matrix.info/index.htm

```html
<!DOCTYPE html>
<html lang="de">
<head>
<meta charset="utf-8">
<title>KORVAN Industrieboden – Unsere Projekte</title>
<link href="https://fonts.googleapis.com/css2?family=Mulish:wght@400;600;700&display=swap" rel="stylesheet">
<style>
:root{
  --page:#ffffff;
  --ink:#1c1c1c;
  --muted:#8a8a8a;
  --line:#d9d9d9;
  --accent:#f5e33a;
  --header:#2f3439;
  --panel:#f0f0f0;
  --backdrop:rgba(0,0,0,.69);
}
*{margin:0;padding:0;box-sizing:border-box}
html,body{width:1102px;height:1200px;overflow:hidden}
body{position:relative;background:var(--page);font-family:'Mulish',sans-serif;color:var(--ink)}
.hero{position:absolute;left:0;top:0;width:1102px;height:284px;background:linear-gradient(160deg,#3a3f44,#2b2f33 55%,#33383d)}
.hero-title{position:absolute;top:80px;width:100%;text-align:center;font-size:33px;font-weight:600;color:#e6e6e6}
.panel{position:absolute;left:95px;top:155px;width:912px;height:470px;background:var(--panel)}
.gallery{position:absolute;left:129px;top:190px;width:842px;height:420px;display:grid;grid-template-columns:repeat(4,1fr);grid-template-rows:repeat(2,1fr)}
.tile{display:block}
.t1{background:linear-gradient(180deg,#dfe3e6,#b8b2aa)}
.t2{background:linear-gradient(135deg,#2a2a2a,#c9c7c3 50%,#2a2a2a)}
.t3{background:linear-gradient(180deg,#1d2a3a,#304258)}
.t4{background:linear-gradient(120deg,#d6d6d6,#5e5e5e 60%,#0e0e0e)}
.t5{background:linear-gradient(170deg,#cfc7bd,#a79d90 55%,#8c8277)}
.t6{background:linear-gradient(180deg,#bdb8b0,#8f8a83)}
.t7{background:linear-gradient(180deg,#9aa0a6,#6b7076)}
.t8{background:linear-gradient(160deg,#8a8783,#6a6763)}
.intro{position:absolute;top:644px;width:100%;text-align:center;font-size:10px;line-height:16px}
.social{position:absolute;top:708px;left:0;width:100%;height:30px}
.social a{position:absolute;top:0;width:60px;margin-left:-30px;text-align:center;font-size:9px;font-weight:700;color:var(--ink);text-decoration:none}
.social a::before{content:"";display:block;width:20px;height:20px;margin:0 auto 3px;border-radius:50%;background:var(--ink)}
.btn{position:absolute;display:flex;align-items:center;justify-content:center;gap:8px;background:var(--accent);font-size:9px;font-weight:700;color:var(--ink);text-transform:uppercase;border:0}
.btn-project{left:433px;top:768px;width:235px;height:27px}
.btn-contact{left:471px;top:1076px;width:159px;height:27px}
.map-deco{position:absolute;left:673px;top:769px;width:251px;height:340px;background:radial-gradient(ellipse at center,#f3f3f3 55%,rgba(243,243,243,0) 72%)}
.contact-title{position:absolute;left:129px;top:868px;font-size:21px;font-weight:600}
.contact-text{position:absolute;left:129px;top:928px;width:420px;font-size:10px;line-height:16px}
.info{position:absolute;top:983px;font-size:14px;line-height:21px}
.info .row{position:relative;padding-left:16px}
.info svg{position:absolute;left:0;top:4px;width:11px;height:12px;fill:var(--ink)}
.info strong{font-weight:600}
.c1{left:129px}.c2{left:421px}.c3{left:715px}
.footer-line{position:absolute;left:129px;top:1149px;width:844px;height:1px;background:#333}
.footer{position:absolute;top:1162px;left:129px;width:844px;font-size:8px;color:#777;display:flex;justify-content:space-between}
.footer nav span{margin-right:12px;text-transform:uppercase}
.backdrop{position:absolute;inset:0;background:var(--backdrop)}
.modal{position:absolute;left:331px;top:217px;width:440px;height:404px;background:var(--page)}
.modal-close{position:absolute;right:16px;top:11px;width:12px;height:12px}
.modal h2{position:absolute;top:36px;width:100%;text-align:center;font-size:21px;font-weight:700}
.modal p{position:absolute;top:72px;left:40px;right:40px;text-align:center;font-size:10px;line-height:16px}
.field{position:absolute}
.field label{display:block;font-size:8.5px;color:var(--muted);text-transform:uppercase;height:9px;line-height:9px;margin-bottom:6px}
.field span{display:block;border:1px solid var(--line);height:28px}
.f1{left:18px;top:128px;width:199px}
.f2{left:223px;top:128px;width:199px}
.f3{left:18px;top:183px;width:199px}
.f4{left:223px;top:183px;width:199px}
.f5{left:18px;top:237px;width:404px}
.f5 span{height:57px}
.btn-send{left:158px;top:342px;width:122px;height:27px}
</style>
</head>
<body>
<header class="hero" role="img" aria-label="Dunkle Betonwand-Textur als Hintergrund">
  <h1 class="hero-title">Unsere Projekte</h1>
</header>
<section class="panel"></section>
<div class="gallery">
  <span class="tile t1" role="img" aria-label="Projektfoto: Betonfassade vor hellem Himmel"></span>
  <span class="tile t2" role="img" aria-label="Projektfoto: Betonträger in Schrägansicht"></span>
  <span class="tile t3" role="img" aria-label="Projektfoto: Gebäude bei Nacht"></span>
  <span class="tile t4" role="img" aria-label="Projektfoto: Betontreppe mit Durchgang"></span>
  <span class="tile t5" role="img" aria-label="Projektfoto: Betonstützen unter einer Überdachung"></span>
  <span class="tile t6" role="img" aria-label="Projektfoto: Betonhalle"></span>
  <span class="tile t7" role="img" aria-label="Projektfoto: moderne Betonarchitektur"></span>
  <span class="tile t8" role="img" aria-label="Projektfoto: Sichtbetonfläche im Detail"></span>
</div>
<p class="intro">Lorem ipsum dolor sit amet consectetur. Tincidunt eu amet sed scelerisque nisi vel.<br>Risus fermentum non massa vel quam aliquam</p>
<nav class="social">
  <a href="#" style="left:460px">Plauda</a>
  <a href="#" style="left:519px">Berufo</a>
  <a href="#" style="left:579px">Xantel</a>
  <a href="#" style="left:641px">Fotara</a>
</nav>
<a class="btn btn-project">Erzählen Sie uns von Ihrem Projekt</a>

<div class="map-deco" role="img" aria-label="Dezente Deutschlandkarte als Hintergrunddekoration"></div>
<h2 class="contact-title">Kontaktieren sie uns</h2>
<p class="contact-text">Bei Fragen zu unseren Leistungen und Angeboten, schreiben Sie uns eine Email oder rufen Sie uns an. Wir arbeiten in ganz Deutschland</p>
<div class="info c1">
  <div class="row"><svg viewBox="0 0 12 16"><path d="M6 0a6 6 0 0 0-6 6c0 4.5 6 10 6 10s6-5.5 6-10a6 6 0 0 0-6-6zm0 8.5A2.5 2.5 0 1 1 6 3.5a2.5 2.5 0 0 1 0 5z"/></svg><strong>KORVAN Industrieboden GmbH</strong><br>Lindenhofweg 7<br>08301 Zwönitztal</div>
</div>
<div class="info c2">
  <div class="row"><svg viewBox="0 0 16 16"><path d="M3.5 0l3 3.5-2 2a10 10 0 0 0 6 6l2-2 3.5 3-2 3.5C7 15.5.5 9 0 2z"/></svg>03771 4820163<br>03 76 05 / 41 27 59</div>
  <div class="row"><svg viewBox="0 0 10 16"><path d="M1 0h8a1 1 0 0 1 1 1v14a1 1 0 0 1-1 1H1a1 1 0 0 1-1-1V1a1 1 0 0 1 1-1zm1 2v11h6V2z"/></svg>Mobil - 0171 8264093</div>
</div>
<div class="info c3">
  <div class="row"><svg viewBox="0 0 16 14"><path d="M4 0h8v4H4zM0 5h16v6h-3v3H3v-3H0zm5 4v3h6V9z"/></svg>037605 412760<br>03 76 05 / 41 27 60</div>
  <div class="row"><svg viewBox="0 0 16 12"><path d="M0 0h16v2L8 7 0 2zm0 4l8 5 8-5v8H0z"/></svg>info@korvan-industrieboden.de</div>
</div>
<a class="btn btn-contact">Kontaktieren sie uns</a>
<div class="footer-line"></div>
<footer class="footer">
  <nav><span>Impressum</span><span>Datenschutz</span></nav>
  <div>Copyright © 2023 KORVAN Industrieboden GmbH - Alle Rechte vorbehalten</div>
</footer>

<div class="backdrop"></div>
<div class="modal" role="dialog" aria-label="Kontaktformular">
  <svg class="modal-close" viewBox="0 0 12 12"><path d="M0 0L12 12M12 0L0 12" stroke="#1c1c1c" stroke-width="1.4"/></svg>
  <h2>Kontaktieren sie uns</h2>
  <p>Lorem ipsum dolor sit amet consectetur. Tincidunt eu amet sed scelerisque nisi vel. Risus fermentum non massa vel quam aliquam</p>
  <div class="field f1"><label>Vorname</label><span></span></div>
  <div class="field f2"><label>Nachname</label><span></span></div>
  <div class="field f3"><label>Email</label><span></span></div>
  <div class="field f4"><label>Telefon</label><span></span></div>
  <div class="field f5"><label>Nachricht</label><span></span></div>
  <a class="btn btn-send">Schicken <svg width="12" height="11" viewBox="0 0 12 11"><path d="M12 0L0 5l3.5 1.5L10 2 4.5 7.2V11l2-2.6L9 10z" fill="#1c1c1c"/></svg></a>
</div>
</body>
</html>
```